resdesign signage banners for mortgage broking firm rates

Kestrel Rise logo at the top
Bank logos down the bottom
Rates box white, with blue writing
"Variable Rate Today!"
(space for rates, change all the time)
Variable Rate Comparison Rate

Fixed Rate Today!

Fixed rate Comparsion rate

The backgroud should be blue and fade down to white with the logos at the bottom

Below the rates boxes

should have

"Kestrel Rise returns 0.15% to you every year! That is $750 on $500,000 loan."

attached is pictures of the previous banners

1.4m L
80 cm W
for the pull up banner

We want the banner similar, just a new updated design.
Updates

Project Deadline Extended Reason: The managing director came back and thought the design looked to busy, he wants a simpler design similar to previous. Added Wednesday, April 20, 2016

Industry/Entity Type

Finance

Colors
fbee3d
fbed22
33a6d7
0292cd
ffffff

Requirements
Must have
• Bank logos down the bottom
• Rates section for variable and fixed
• Kestrel Rise Home Loan logo
• Blue writing
• white back ground for rates box.
• Fade from sky blue at the top down to white where to logos are
• The cloud behind the logo like the attached picture.
Nice to have
• New modern design

```html
<!DOCTYPE html>
<html lang="en">
<head>
<meta charset="utf-8">
<title>Kestrel Rise Home Loans – Rates Banner</title>
<link href="https://fonts.googleapis.com/css2?family=Exo+2:wght@600;700;800&family=Encode+Sans+Semi+Condensed:wght@700&display=swap" rel="stylesheet">
<style>
  :root {
    --sky: #00aeef;
    --sky-deep: #0292cd;
    --navy: #1d3f63;
    --orange: #f05a28;
    --coral: #f26b3a;
    --white: #ffffff;
    --frame: #a9d3ee;
  }
  * { box-sizing: border-box; margin: 0; padding: 0; }
  html, body { width: 1155px; height: 1200px; overflow: hidden; background: var(--white); }
  .canvas { position: relative; width: 1155px; height: 1200px; }

  .banner {
    position: absolute; left: 246px; top: 20px;
    width: 663px; height: 1160px;
    background: linear-gradient(to bottom, var(--sky) 0, var(--sky) 800px, var(--white) 890px, var(--white) 100%);
    border: 1px solid #333;
    box-shadow: 4px 4px 6px rgba(0,0,0,.35);
    overflow: hidden;
  }

  /* Brand name placeholder */
  .brand {
    position: absolute; left: 0; top: 34px; width: 100%; height: 130px;
    display: flex; align-items: center; justify-content: center; gap: 18px;
  }
  .brand-dot { width: 70px; height: 70px; border-radius: 50%; background: var(--white); flex: none; }
  .brand-name {
    font-family: "Exo 2", sans-serif; font-weight: 800; color: var(--navy);
    line-height: 1; text-align: left;
  }
  .brand-name .line-main { display: block; font-size: 62px; letter-spacing: -1px; }
  .brand-name .line-sub { display: block; font-size: 30px; letter-spacing: 9px; margin-top: 8px; }

  /* Rate panels */
  .rate-panel {
    position: absolute; left: 21px; width: 620px; height: 298px;
    background: var(--white); border: 1.5px solid var(--coral); border-radius: 14px;
  }
  .rate-panel.variable { top: 191px; }
  .rate-panel.fixed { top: 531px; }
  .rate-title {
    position: absolute; left: 0; top: 6px; width: 100%; text-align: center;
    font-family: "Exo 2", sans-serif; font-weight: 700; font-variant: small-caps;
    font-size: 46px; color: var(--navy); letter-spacing: 2px; line-height: 52px;
  }
  .rate-slot {
    position: absolute; top: 63px; width: 260px; height: 177px;
    border: 1px solid var(--frame); background: var(--white);
  }
  .rate-slot.left { left: 35px; }
  .rate-slot.right { left: 325px; }
  .rate-label {
    position: absolute; top: 248px; width: 300px; text-align: center;
    font-family: "Exo 2", sans-serif; font-weight: 700; font-variant: small-caps;
    font-size: 30px; color: var(--navy); letter-spacing: 1.5px; line-height: 36px;
  }
  .rate-label.left { left: 15px; }
  .rate-label.right { left: 305px; }

  /* Offer */
  .offer { position: absolute; left: 0; top: 880px; width: 100%; text-align: center;
    font-family: "Encode Sans Semi Condensed", sans-serif; font-weight: 700; font-size: 31px; line-height: 44px; }
  .offer-lead { color: var(--sky-deep); display: block; letter-spacing: -.4px; }
  .offer-detail { color: var(--orange); display: block; }

  .divider { position: absolute; left: 0; top: 981px; width: 100%; height: 6px; background: var(--sky-deep); }

  /* Lender names */
  .lenders {
    position: absolute; left: 18px; top: 1008px; width: 627px;
    display: grid; grid-template-columns: repeat(3, 1fr); row-gap: 14px; column-gap: 10px;
    list-style: none;
  }
  .lender {
    display: flex; align-items: center; justify-content: center; gap: 8px; height: 38px;
    font-family: "Exo 2", sans-serif; font-weight: 700; font-size: 26px; line-height: 1;
  }
  .lender-mark { width: 18px; height: 18px; flex: none; }
  .lender-mark.round { border-radius: 50%; }
  .lender.harbor { color: #2b3e73; font-size: 22px; letter-spacing: 2px; }
  .lender.marlow { color: #cc2229; }
  .lender.cobalt { color: #1b5d7c; font-size: 22px; }
  .lender.peakline { color: #0072bc; font-size: 30px; }
  .lender.ashgrove { color: #1b2452; }
  .lender.summit { color: #9a1b1f; }
  .lender.fernvale { color: #1c4c8c; font-size: 30px; font-weight: 600; }
  .lender.redmark { color: #d5002b; }
  .lender.westvale { color: #f7941d; }
</style>
</head>
<body>
<main class="canvas">
  <section class="banner" aria-label="Kestrel Rise Home Loans rates banner">

    <header class="brand">
      <span class="brand-dot"></span>
      <h1 class="brand-name">
        <span class="line-main">Kestrel Rise</span>
        <span class="line-sub">HOME LOANS</span>
      </h1>
    </header>

    <article class="rate-panel variable">
      <h2 class="rate-title">Variable Rate Today!</h2>
      <div class="rate-slot left"></div>
      <div class="rate-slot right"></div>
      <p class="rate-label left">Variable Rate</p>
      <p class="rate-label right">Comparison Rate</p>
    </article>

    <article class="rate-panel fixed">
      <h2 class="rate-title">Fixed Rate Today!</h2>
      <div class="rate-slot left"></div>
      <div class="rate-slot right"></div>
      <p class="rate-label left">Fixed Rate</p>
      <p class="rate-label right">Comparison Rate</p>
    </article>

    <p class="offer">
      <span class="offer-lead">Kestrel Rise returns 0.15% to you every year!</span>
      <span class="offer-detail">That is $750 on $500,000 loan.</span>
    </p>

    <div class="divider"></div>

    <ul class="lenders">
      <li class="lender harbor">HARBOR DIRECT</li>
      <li class="lender marlow"><span class="lender-mark round" style="background:#5aa832"></span>marlow</li>
      <li class="lender cobalt">COBALT BANK</li>
      <li class="lender peakline">PEAKLINE</li>
      <li class="lender ashgrove">Ashgrove<span class="lender-mark round" style="background:#2aa8e0"></span></li>
      <li class="lender summit"><span class="lender-mark" style="background:#f7c21b"></span>Summit Bank</li>
      <li class="lender fernvale">fernvale</li>
      <li class="lender redmark"><span class="lender-mark" style="background:#d5002b"></span>Redmark</li>
      <li class="lender westvale">westvale</li>
    </ul>

  </section>
</main>
</body>
</html>
```